Pharmaceutical Manufacturing Services Advertisement

We need a new full page advertisement designed for publication in international magazines. We are a custom pharmaceutical manufacturing company and we help biotechnology companies scale up their drug development for clinical trials. The products we help manufacture are therapeutics for global healthcare problems.

Target Market(s)

Verott Bio is a privately owned contract development manufacturing organisation (CDMO) headquartered in Darra, QLD, Australia.

Our mission is to is to be a global leader in development and in the provision of contract manufacturing for active pharmaceutical ingredient processes.

Why we do what we Do:

To help advance Biotechnology Companies so that they can deliver innovative therapeutics
~ enabling patients to live longer, healthier and happier lives
~ which solves worldwide health problems

Verott Bio’s role is to develop, implement and scale up the production to deliver biologic medicines for patients in partnership with the biotechnology companies.

Industry/Entity Type

Biotechnology

Font styles to use
Sans Serif

Colors

Designer to choose colors to be used in the design.

Requirements
Must have
• Please see the script on the Word document. There are 4 optional Header Taglines. Additional ideas for multiple designs for the taglines welcomed.
• However preference is for either of the first two:
• 1. Building your vision for better healthcare
• 2. Bridging your vision for better healthcare
• File Specs:
• • All artwork should be submitted as high-resolution (300 min. dpi), press-ready PDF files
• • CMYK color only
• • Full page 8.25” x 10.812”; 209.55 x 274.62 mm
• • Live Area for all sizes: 0.25” (6.35 mm) inside the trim
• • Bleed Area for all sizes: Extends 0.125” (3.175 mm) from trim
Nice to have
• Modern Science look to inspire biotechnology companies to work with us.
• Search for images to use by keyword "recombinant dna"

```html
<!DOCTYPE html>
<html lang="en">
<head>
<meta charset="utf-8">
<title>Verott Bio – Full Page Advertisement</title>
<link href="https://fonts.googleapis.com/css2?family=Montserrat:wght@400;500;600;700&family=Oswald:wght@400;600&display=swap" rel="stylesheet">
<style>
  :root {
    --navy: #0b3a5d;
    --navy-deep: #07304f;
    --green: #9cb52b;
    --ink: #1d1d1f;
    --paper: #ffffff;
    --photo-light: #dfe5e8;
    --photo-mid: #b9c6cc;
  }
  * { box-sizing: border-box; margin: 0; padding: 0; }
  html, body { width: 960px; height: 1200px; overflow: hidden; background: var(--paper); }
  .ad-page {
    position: relative; width: 960px; height: 1200px; overflow: hidden;
    background: var(--paper); font-family: "Montserrat", sans-serif; color: var(--ink);
  }
  .side-panel {
    position: absolute; left: 545px; top: 0; width: 415px; height: 1200px;
    background: linear-gradient(160deg, var(--navy) 0%, var(--navy-deep) 100%);
  }
  .hero-photo {
    position: absolute; left: 0; top: 57px; width: 781px; height: 499px;
    background: var(--paper); padding: 0 7px 7px 0;
  }
  .hero-photo__fill {
    width: 100%; height: 100%;
    background: linear-gradient(120deg, var(--photo-light) 0%, #c9d3d8 45%, #eef1f2 70%, var(--photo-mid) 100%);
  }
  .copy-column { position: absolute; left: 68px; top: 608px; width: 424px; }
  .headline__lead { font-size: 40px; font-weight: 400; letter-spacing: 0.5px; line-height: 1.05; white-space: nowrap; }
  .headline__accent {
    font-family: "Oswald", sans-serif; font-weight: 600; color: var(--green);
    font-size: 39px; line-height: 1.1; letter-spacing: 0; white-space: nowrap;
  }
  .headline__sub { margin-top: 6px; font-size: 13px; font-weight: 600; white-space: nowrap; }
  .intro { margin-top: 34px; font-size: 9.5px; line-height: 1.42; text-align: justify; }
  .intro p + p { margin-top: 12px; }
  .brand { position: absolute; left: 72px; top: 926px; }
  .brand__name {
    display: flex; align-items: center; gap: 12px;
    font-size: 48px; font-weight: 600; color: var(--navy); line-height: 1; letter-spacing: 1px;
  }
  .brand__dot { width: 16px; height: 16px; border-radius: 50%; background: var(--green); }
  .brand__tagline {
    margin-top: 10px; font-family: "Oswald", sans-serif; font-weight: 400;
    font-size: 17px; color: var(--navy); letter-spacing: 0.2px;
  }
  .contact { position: absolute; left: 72px; top: 1035px; font-style: normal; }
  .contact__region { font-size: 20px; font-weight: 500; color: var(--green); }
  .contact__phone { margin-top: 8px; font-size: 25px; font-weight: 400; }
  .contact__line { display: flex; align-items: center; gap: 8px; margin-top: 8px; font-size: 13.5px; }
  .contact__line svg { width: 12px; height: 12px; flex: none; }
  .offer { position: absolute; left: 625px; color: var(--paper); }
  .offer--products { top: 652px; }
  .offer--services { top: 895px; }
  .offer__title { font-size: 26px; font-weight: 600; color: var(--green); margin-bottom: 24px; }
  .offer__list { list-style: none; }
  .offer__item { display: flex; align-items: flex-start; gap: 14px; font-size: 14.5px; line-height: 1.2; margin-bottom: 17px; }
  .offer__item svg { width: 18px; height: 18px; flex: none; margin-top: -3px; }
</style>
</head>
<body>
<main class="ad-page">
  <div class="side-panel"></div>

  <div class="hero-photo">
    <div class="hero-photo__fill" role="img" aria-label="Laboratory photograph of a scientist in a white coat looking into a microscope beside flasks and test tubes"></div>
  </div>

  <div class="copy-column">
    <header class="headline">
      <h1 class="headline__lead">Building your vision</h1>
      <div class="headline__accent">FOR BETTER HEALTHCARE</div>
      <p class="headline__sub">Your Partner in Early Phase Clinical Biomanufacturing</p>
    </header>

    <section class="intro">
      <p>We have been serving the pharmaceutical, biotechnology and veterinary industry for over 20 years so you can create innovative medicines for worldwide health problems.</p>
      <p>Get your therapeutics to the patient faster with cost-effective manufacturing for your GMP clinical trial material. We offer rapid technology transfer, scale-up development and manufacturing of microbial cell-derived proteins at up to 500L scale. We prepare your active pharmaceutical ingredient (API) products to a world class standard ready for clinical development.</p>
    </section>
  </div>

  <div class="brand">
    <div class="brand__name">VEROTT BIO <span class="brand__dot"></span></div>
    <div class="brand__tagline">BIOPHARMACEUTICAL MANUFACTURING</div>
  </div>

  <address class="contact">
    <div class="contact__region">Australia</div>
    <div class="contact__phone">+61(7)30418852</div>
    <div class="contact__line">
      <svg viewBox="0 0 12 12"><rect x="0.5" y="2" width="11" height="8" fill="#9cb52b"/><path d="M0.5 2 L6 6.5 L11.5 2" fill="none" stroke="#fff" stroke-width="1"/></svg>
      enquiries@verottbio.com.au
    </div>
    <div class="contact__line">
      <svg viewBox="0 0 12 12"><circle cx="6" cy="6" r="5.5" fill="#9cb52b"/><path d="M0.5 6 H11.5 M6 0.5 C3 3.5 3 8.5 6 11.5 M6 0.5 C9 3.5 9 8.5 6 11.5" fill="none" stroke="#fff" stroke-width="0.8"/></svg>
      www.verottbio.com.au
    </div>
  </address>

  <section class="offer offer--products">
    <h2 class="offer__title">Products</h2>
    <ul class="offer__list">
      <li class="offer__item"><svg viewBox="0 0 18 18"><rect x="1" y="3" width="13" height="13" fill="none" stroke="#9cb52b" stroke-width="1.6"/><path d="M4.5 9 L7.5 12 L16 2" fill="none" stroke="#9cb52b" stroke-width="1.8"/></svg>Recombinant proteins</li>
      <li class="offer__item"><svg viewBox="0 0 18 18"><rect x="1" y="3" width="13" height="13" fill="none" stroke="#9cb52b" stroke-width="1.6"/><path d="M4.5 9 L7.5 12 L16 2" fill="none" stroke="#9cb52b" stroke-width="1.8"/></svg>Live Biotherapeutics</li>
      <li class="offer__item"><svg viewBox="0 0 18 18"><rect x="1" y="3" width="13" height="13" fill="none" stroke="#9cb52b" stroke-width="1.6"/><path d="M4.5 9 L7.5 12 L16 2" fill="none" stroke="#9cb52b" stroke-width="1.8"/></svg>Bacterial vaccines</li>
      <li class="offer__item"><svg viewBox="0 0 18 18"><rect x="1" y="3" width="13" height="13" fill="none" stroke="#9cb52b" stroke-width="1.6"/><path d="M4.5 9 L7.5 12 L16 2" fill="none" stroke="#9cb52b" stroke-width="1.8"/></svg>Plasmid DNA</li>
    </ul>
  </section>

  <section class="offer offer--services">
    <h2 class="offer__title">Services</h2>
    <ul class="offer__list">
      <li class="offer__item"><svg viewBox="0 0 18 18"><rect x="1" y="3" width="13" height="13" fill="none" stroke="#9cb52b" stroke-width="1.6"/><path d="M4.5 9 L7.5 12 L16 2" fill="none" stroke="#9cb52b" stroke-width="1.8"/></svg>Bacterial / Yeast Fermentation</li>
      <li class="offer__item"><svg viewBox="0 0 18 18"><rect x="1" y="3" width="13" height="13" fill="none" stroke="#9cb52b" stroke-width="1.6"/><path d="M4.5 9 L7.5 12 L16 2" fill="none" stroke="#9cb52b" stroke-width="1.8"/></svg>Cell Banking</li>
      <li class="offer__item"><svg viewBox="0 0 18 18"><rect x="1" y="3" width="13" height="13" fill="none" stroke="#9cb52b" stroke-width="1.6"/><path d="M4.5 9 L7.5 12 L16 2" fill="none" stroke="#9cb52b" stroke-width="1.8"/></svg>Process Development/Scale-up</li>
      <li class="offer__item"><svg viewBox="0 0 18 18"><rect x="1" y="3" width="13" height="13" fill="none" stroke="#9cb52b" stroke-width="1.6"/><path d="M4.5 9 L7.5 12 L16 2" fill="none" stroke="#9cb52b" stroke-width="1.8"/></svg>cGMP Manufacture of<br>biopharmaceutical APIs</li>
      <li class="offer__item"><svg viewBox="0 0 18 18"><rect x="1" y="3" width="13" height="13" fill="none" stroke="#9cb52b" stroke-width="1.6"/><path d="M4.5 9 L7.5 12 L16 2" fill="none" stroke="#9cb52b" stroke-width="1.8"/></svg>Stability Testing</li>
    </ul>
  </section>
</main>
</body>
</html>
```